Cookie needs a website

We need a website for a cookie company based in Mexico City. Our company (called Hornos Lucero) has been baking and crating all sorts of cookies and cakes for more than 35 years.
We started off as a family business and till this date we are still functioning as one. We need the design of the web to be more on the baking side as we have many types of cookies cakes, pastries & muffins. Key elements, home style baking, use colours black, white and red. Tabs we need: front page, who are we, our brands and contact Preferable in Spanish. Im sure you have questions, please contact us. This is for homepage PSD design only no CSS,XHTML or full website build or coding involved as this is design competition.
Updates

Some more information has been added. Thanks is advance for your talent!

Target Market(s)

Target is general public, mostly families. Our product is not a luxury good,more like an affordable treat, however we do use very high quality products and high quality standards. Our motive is natural ingredients and home baked goods.
Our main point of sales is having shops inside department stores. Our own shops and selling to other businesses for re sale

Industry/Entity Type

Business

Font styles to use
Serif

Colors
ec2027
ffffff
333333

Requirements
Must have
• Baking oriented. An oven would be nice since we bake in front of our clients.
Colors we use also important
Nice to have
• make it home. (you have design freedom)
Below are the logos HL is the company name. Pimbos is one of our branches and the the pictures are from the cookies we make
Should not have
• PLEASE NO corny, over colorfull or tacky designs!!

```html
<!DOCTYPE html>
<html lang="en">
<head>
<meta charset="utf-8">
<title>Hornos Lucero</title>
<link href="https://fonts.googleapis.com/css2?family=Dancing+Script:wght@700&family=Raleway:wght@400;500&family=Open+Sans:wght@400;600&display=swap" rel="stylesheet">
<style>
:root{
  --red:#ec2027;
  --red-dark:#b9161c;
  --white:#ffffff;
  --ink:#111111;
  --grey-band:#efefef;
  --text-soft:#555555;
  --footer:#3a3a3a;
}
*{margin:0;padding:0;box-sizing:border-box}
html,body{width:1200px;height:2316px;overflow:hidden}
body{position:relative;background:var(--white);font-family:"Open Sans",Arial,sans-serif;color:var(--ink)}
.abs{position:absolute}

/* hero */
.hero{left:0;top:0;width:1200px;height:566px;
  background:
    radial-gradient(ellipse 520px 150px at 50% 108%,rgba(70,150,170,.55) 0%,rgba(70,150,170,0) 70%),
    radial-gradient(ellipse 320px 260px at 0% 0%,rgba(60,120,140,.7) 0%,rgba(60,120,140,0) 70%),
    radial-gradient(ellipse 320px 260px at 100% 0%,rgba(60,110,130,.7) 0%,rgba(60,110,130,0) 70%),
    radial-gradient(ellipse 600px 330px at 55% 50%,#c89a62 0%,#a97a4a 35%,#7a5535 65%,#3e3a36 100%)}
.nav-bar{left:0;top:0;width:1200px;height:72px;border-bottom:1px solid rgba(255,255,255,.15)}
.nav-link{top:22px;height:30px;line-height:30px;color:var(--white);font-size:18px;padding:0 10px;border-radius:3px}
.nav-link.active{background:var(--red)}
.brand-mark{left:552px;top:28px;width:96px;height:96px;border-radius:50%;background:var(--red);border:4px solid var(--white);
  color:var(--white);font-size:30px;font-weight:600;text-align:center;line-height:88px}
.hero-title{left:115px;top:212px;width:800px;text-align:center;color:var(--white);font-family:"Dancing Script",cursive;font-size:90px;line-height:102px}
.slider-arrow{top:238px;width:54px;height:54px;border-radius:50%}
.slider-arrow.prev{left:42px;background:rgba(180,30,40,.75)}
.slider-arrow.next{left:1103px;background:rgba(20,20,20,.75)}
.slider-arrow svg{position:absolute;left:17px;top:17px}

/* categories */
.categories{left:0;top:566px;width:1200px;height:318px;background:var(--grey-band)}
.category{top:68px;width:220px;text-align:center}
.category-icon{width:92px;height:76px;margin:0 auto;border-radius:18px;
  background:radial-gradient(ellipse at 50% 50%,#ec2027 0%,rgba(236,32,39,.85) 40%,rgba(236,32,39,.25) 75%,rgba(236,32,39,0) 100%)}
.category-name{margin-top:12px;font-family:"Raleway",sans-serif;font-size:28px;font-weight:500;line-height:34px}
.category-text{margin-top:8px;font-size:11px;line-height:20.5px;color:var(--text-soft)}

/* popular */
.section-title{left:0;width:1200px;text-align:center;color:var(--red);font-family:"Raleway",sans-serif;font-size:27px;font-weight:500}
.section-sub{left:0;width:1200px;text-align:center;font-size:12.5px;font-weight:600}
.filter{top:1004px;width:79px;height:27px;border:1px solid #444;border-radius:4px;text-align:center;line-height:25px;font-size:11px;color:var(--red)}
.filter.active{background:var(--red);color:var(--white);border-color:var(--red-dark)}
.product{top:1054px;width:301px;height:303px}
.p1{left:124px;background:
  radial-gradient(ellipse 70px 80px at 95% 22%,#2a2c48 0%,rgba(42,44,72,0) 100%),
  radial-gradient(ellipse 90px 110px at 30% 42%,#5a2418 0%,rgba(90,36,24,0) 100%),
  radial-gradient(ellipse 100px 110px at 66% 58%,#4a1e16 0%,#6a2c1f 45%,rgba(106,44,31,0) 100%),
  linear-gradient(180deg,#dfe2dc 0%,#e9ebe6 60%,#f6f6f3 78%,#b9bdb7 100%)}
.p2{left:451px;background:
  radial-gradient(circle at 50% 52%,#f08a58 0%,#e8614a 30%,rgba(232,97,74,0) 60%),
  radial-gradient(ellipse at 50% 50%,#e2574a 0%,#cf3f3a 60%,#9c2428 100%)}
.p3{left:775px;background:
  radial-gradient(ellipse 70px 50px at 14% 10%,#c0262c 0%,rgba(192,38,44,0) 100%),
  radial-gradient(ellipse 120px 110px at 52% 52%,#e6d2b8 0%,#a07550 35%,#5a3a26 70%,rgba(40,28,20,0) 100%),
  linear-gradient(180deg,#161210 0%,#1d1814 100%)}
.zoom{left:119px;top:120px;width:62px;height:62px;border-radius:50%;background:rgba(40,40,40,.75)}
.zoom svg{position:absolute;left:18px;top:18px}

/* about */
.about-art{left:155px;top:1558px;width:550px;height:349px;background:radial-gradient(ellipse at 42% 52%,#d9d9d9 0%,#ececec 45%,#ffffff 80%)}
.about-text{left:570px;top:1569px;width:512px;font-size:13px;line-height:31px}
.about-text p + p{margin-top:2px}

/* footer */
.footer{left:0;top:1936px;width:1200px;height:380px;background:var(--footer);color:var(--white)}
.footer-heading{top:44px;font-family:"Raleway",sans-serif;font-size:22px;font-weight:400}
.branch-card{left:126px;top:96px;width:168px;height:144px;background:var(--white);color:var(--ink);
  font-weight:600;font-size:26px;text-align:center;line-height:144px}
.links-label{left:126px;top:260px;font-family:"Raleway",sans-serif;font-size:16px}
.social{top:294px;width:28px;height:28px;border-radius:4px}
.contact-item{left:368px;font-size:13px;line-height:16px}
.contact-item svg{position:absolute;left:0;top:1px}
.contact-item span{position:absolute;left:26px;top:0;width:190px}
.quick-links{left:612px;top:96px;list-style:none;font-size:13px;font-weight:600}
.quick-links li{height:25.5px;position:relative;padding-left:22px}
.quick-links li::before{content:"";position:absolute;left:2px;top:5px;width:10px;height:10px;border-radius:50%;background:var(--white)}
.subscribe-text{left:859px;top:78px;width:210px;font-size:13px;line-height:16px}
.subscribe-field{left:857px;top:133px;width:216px;height:39px;border-radius:8px;background:var(--red);border:2px solid var(--red-dark)}
.subscribe-field span{position:absolute;left:12px;top:9px;font-size:12px;font-style:italic;color:rgba(255,255,255,.6)}
.subscribe-field svg{position:absolute;right:14px;top:11px}
</style>
</head>
<body>

<header class="abs hero" role="img" aria-label="Photo of home-baked cookies inside an open bag">
  <div class="abs nav-bar"></div>
  <a class="abs nav-link active" style="left:292px">Home</a>
  <a class="abs nav-link" style="left:398px">Who We Are</a>
  <div class="abs brand-mark">HL</div>
  <a class="abs nav-link" style="left:672px">Our Brands</a>
  <a class="abs nav-link" style="left:818px">Contact us</a>
  <h1 class="abs hero-title">WE implament Your<br>Delicios Dreams</h1>
  <div class="abs slider-arrow prev"><svg width="20" height="20" viewBox="0 0 20 20"><path d="M13 3 L6 10 L13 17" stroke="#fff" stroke-width="3.5" fill="none"/></svg></div>
  <div class="abs slider-arrow next"><svg width="20" height="20" viewBox="0 0 20 20"><path d="M7 3 L14 10 L7 17" stroke="#fff" stroke-width="3.5" fill="none"/></svg></div>
</header>

<section class="abs categories">
  <div class="abs category" style="left:121px"><div class="category-icon" role="img" aria-label="Red cake icon"></div><h3 class="category-name">Cakes</h3><p class="category-text">It is a long established fact that a<br>reader will be distracted by the read-<br>able content of a page when looking<br>at its layout.</p></div>
  <div class="abs category" style="left:366px"><div class="category-icon" role="img" aria-label="Red pastry slice icon"></div><h3 class="category-name">Pastries</h3><p class="category-text">It is a long established fact that a<br>reader will be distracted by the read-<br>able content of a page when looking<br>at its layout.</p></div>
  <div class="abs category" style="left:605px"><div class="category-icon" role="img" aria-label="Red muffin icon"></div><h3 class="category-name">Muffins</h3><p class="category-text">It is a long established fact that a<br>reader will be distracted by the read-<br>able content of a page when looking<br>at its layout.</p></div>
  <div class="abs category" style="left:860px"><div class="category-icon" role="img" aria-label="Red cookie icon"></div><h3 class="category-name">Cookies</h3><p class="category-text">It is a long established fact that a<br>reader will be distracted by the read-<br>able content of a page when looking<br>at its layout.</p></div>
</section>

<h2 class="abs section-title" style="top:918px">Most Populare Items</h2>
<p class="abs section-sub" style="top:961px">Our services are the best in town, we provide great quality baked products</p>
<div class="abs filter" style="left:378px">All items</div>
<div class="abs filter" style="left:474px">Cakes</div>
<div class="abs filter" style="left:570px">Pastries</div>
<div class="abs filter active" style="left:667px">Muffins</div>
<div class="abs filter" style="left:763px">Cookies</div>
<div class="abs product p1" role="img" aria-label="Photo of chocolate muffins on a plate"></div>
<div class="abs product p2" role="img" aria-label="Photo of a red jelly pastry">
  <div class="abs zoom"><svg width="26" height="26" viewBox="0 0 26 26"><circle cx="11" cy="11" r="8" stroke="#fff" stroke-width="3" fill="none"/><path d="M17 17 L24 24" stroke="#fff" stroke-width="3.5"/><path d="M7 11 H15 M11 7 V15" stroke="#fff" stroke-width="2.5"/></svg></div>
</div>
<div class="abs product p3" role="img" aria-label="Photo of a glazed crumb muffin with strawberries"></div>

<h2 class="abs section-title" style="top:1403px">Who We Are</h2>
<p class="abs section-sub" style="top:1454px">Our services are the best in town, we provide great quality baked products</p>
<div class="abs about-art" role="img" aria-label="Line illustration of a bread basket, donut and croissants"></div>
<div class="abs about-text">
  <p>It is a long established fact that a reader will be distracted by the readable content of a page when looking at its layout. The point of using Lorem Ipsum is that it has a more-or-less normal distribution of letters, as opposed to using 'Content here, content here', making it look like readable English. Many desktop publishing pack-ages</p>
  <p>There are many variations of passages of Lorem Ipsum available, but the majority have suffered alteration in some form</p>
</div>

<footer class="abs footer">
  <h4 class="abs footer-heading" style="left:126px;top:46px">Our Branch</h4>
  <div class="abs branch-card">Pimbos</div>
  <p class="abs links-label">Our Links</p>
  <div class="abs social" style="left:126px;background:#3b5b9a"></div>
  <div class="abs social" style="left:158px;background:#2aa3e0"></div>
  <div class="abs social" style="left:190px;background:#c8232c"></div>
  <div class="abs social" style="left:222px;background:#f08a24"></div>

  <h4 class="abs footer-heading" style="left:368px">Contact Us</h4>
  <div class="abs contact-item" style="top:93px"><svg width="12" height="16" viewBox="0 0 12 16"><path d="M6 0 C2.7 0 0 2.6 0 5.8 C0 10 6 16 6 16 C6 16 12 10 12 5.8 C12 2.6 9.3 0 6 0 Z" fill="#fff"/><circle cx="6" cy="5.8" r="2.2" fill="#3a3a3a"/></svg><span>48,Calle Robles Norte,Col. Arboleda Ciudad Jardín Mexico:04512</span></div>
  <div class="abs contact-item" style="top:150px"><svg width="15" height="15" viewBox="0 0 15 15"><rect width="15" height="15" rx="3" fill="#fff"/><path d="M4 3 L6 3 L7 6 L5.5 7 C6 8.5 7 9.5 8 10 L9 8.5 L12 9.5 L12 11.5 C8 12 3 7 4 3 Z" fill="#3a3a3a"/></svg><span>555-014-2738</span></div>
  <div class="abs contact-item" style="top:181px"><svg width="15" height="15" viewBox="0 0 15 15"><rect width="15" height="15" rx="3" fill="#fff"/><rect x="3" y="4.5" width="9" height="6" fill="#3a3a3a"/><path d="M3 4.5 L7.5 8 L12 4.5" stroke="#fff" stroke-width="1" fill="none"/></svg><span>hola@correo-hl.mx</span></div>

  <h4 class="abs footer-heading" style="left:612px">Populare Links</h4>
  <ul class="abs quick-links"><li>Home</li><li>Who We Are</li><li>Our Brands</li><li>Contact Us</li></ul>

  <h4 class="abs footer-heading" style="left:859px;top:40px">Subscribe</h4>
  <p class="abs subscribe-text">Subscribe to our profile on the following socila networks</p>
  <div class="abs subscribe-field"><span>Enter Email</span><svg width="18" height="13" viewBox="0 0 18 13"><rect width="18" height="13" rx="2" fill="#fff"/><path d="M1 1 L9 7 L17 1" stroke="#ec2027" stroke-width="1.6" fill="none"/></svg></div>
</footer>

</body>
</html>
```